Large Financial Advisory Firm Needs a Brochure!

We are looking for a modern and professional 4 page brochure for our Financial Advisory firm, Harbrook Counsel Group. I've attached multiple files to help with the completion of the design.
SIZE OF BROCHURE: 17 x 11 FLAT, 8.5 x 11 inch FOLDED
1. A PDF titled Design Brief will provide you with an overview of the project, the text to be included in the brochure and other misc. instructions.
2. Logo Files, you will need to incorporate our logo into the brochure design, I've attached all the files please select the images that suit your design.
3. Competitor Illustration - I've attached an image that needs to be included on the 2nd page (inside left cover of the brochure). You will need to incorporate the pros/cons of using our competitors and the advantages of using our firm. This is outlined in the Design Brief PDF.
NOTE: If possible please get rid of the blue sky in the illustration. Just use the buildings, the blue throws off the concept. I contacted the illustrator and am waiting for a design without the sky but it may not be ready in time so please delete it if possible.
- I like the Avenir fonts, 85 Heavy, 65 Medium and 45.

```html
<!DOCTYPE html>
<html lang="en">
<head>
<meta charset="utf-8">
<title>Harbrook Counsel Group – Brochure Covers</title>
<link href="https://fonts.googleapis.com/css2?family=Nunito+Sans:wght@400;600;800;900&display=swap" rel="stylesheet">
<style>
  :root {
    --brand-yellow: #fbbd2b;
    --ink: #141414;
    --paper: #ffffff;
    --stage: #e6e6e6;
    --stripe: #111111;
  }
  * { box-sizing: border-box; margin: 0; padding: 0; }
  html, body { width: 1200px; height: 1055px; overflow: hidden; }
  body {
    background: var(--stage);
    font-family: "Nunito Sans", "Avenir", sans-serif;
    color: var(--ink);
    position: relative;
  }
  .brochure {
    position: absolute;
    left: 20px; top: 152px;
    width: 1160px; height: 751px;
    display: flex;
    box-shadow: 0 6px 24px rgba(0,0,0,0.18);
  }
  .panel {
    width: 580px; height: 100%;
    display: flex; flex-direction: column;
    background: var(--paper);
  }
  .panel__color {
    height: 548px;
    background: var(--brand-yellow);
    position: relative;
  }
  .panel__stripe { height: 9px; background: var(--stripe); }
  .panel__base {
    flex: 1;
    display: flex; align-items: center; justify-content: center;
  }

  /* Back cover */
  .team {
    position: absolute;
    left: 72px; top: 84px;
    width: 440px;
  }
  .team__title {
    font-weight: 900;
    font-size: 24px;
    line-height: 1.1;
    letter-spacing: -0.5px;
    margin-bottom: 8px;
  }
  .team__bios {
    column-count: 2;
    column-gap: 20px;
    column-fill: balance;
    font-size: 8.6px;
    line-height: 1.28;
    text-align: justify;
    hyphens: auto;
  }
  .bio { margin-bottom: 9px; }
  .bio__name {
    display: flex; align-items: flex-start; gap: 4px;
    font-weight: 800; font-size: 10.5px; line-height: 1.15;
    margin-bottom: 2px;
    break-inside: avoid;
    break-after: avoid;
  }
  .bio__mark {
    width: 12px; height: 12px; background: var(--ink); flex: none; margin-top: 2px;
  }
  .bio__role { display: block; }

  .back-name {
    display: flex; align-items: center; gap: 10px;
    font-weight: 800; font-size: 27px; letter-spacing: 0.5px;
    text-transform: uppercase;
  }
  .back-name__square { width: 30px; height: 30px; background: var(--brand-yellow); }

  /* Front cover */
  .front-name {
    position: absolute;
    left: 0; right: 0; top: 240px;
    text-align: center;
    color: var(--paper);
    font-weight: 800;
    font-size: 40px;
    line-height: 1.15;
    letter-spacing: 3px;
    text-transform: uppercase;
  }
  .tagline {
    font-weight: 800;
    font-size: 26px;
    letter-spacing: 0.3px;
  }
</style>
</head>
<body>
  <main class="brochure">
    <section class="panel panel--back">
      <div class="panel__color">
        <div class="team">
          <h2 class="team__title">OUR TEAM</h2>
          <div class="team__bios">
            <article class="bio">
              <h3 class="bio__name"><span class="bio__mark"></span><span>Marcus Hale, CFA, CPA<span class="bio__role">Founder</span></span></h3>
              <p>Marcus works collaboratively with advisors to formulate successful transition plans. He brings creative insight and deep experience to this niche industry that is sorely lacking in both. Prior to his current role, Marcus worked at Crestline Fund Partners where he rose quickly to Regional Director and developed relationships with advisors throughout the Western US. He loved his role at the firm, but became frustrated when some of his closest clients struggled to find the right partner for succession. He witnessed deals implode due to cultural, philosophical, and operational differences and in some cases firms gave up their succession search altogether. He founded Harbrook Counsel Group to make sure advisors find the succession partner they deserve. Marcus earned a bachelor's degree in Finance from Northgate University. He is a Certified Public Accountant and a CFA Charterholder. Marcus enjoys spending time with his wife Elena, traveling internationally, studying foreign languages, and staying active.</p>
            </article>
            <article class="bio">
              <h3 class="bio__name"><span class="bio__mark"></span><span>Owen Reyes, CFA<span class="bio__role">Founder</span></span></h3>
              <p>Owen has over ten years of experience in the financial services industry. Prior to joining Harbrook Counsel Group, he has served as Portfolio Manager and research analyst for various financial service companies, both large and small. Owen wears multiple hats for the organization: he leads the portfolio management team, oversees our operations staff and handles the technological integration between firms. He has been involved in multiple Advisor mergers and transitions and understands the challenges that firms face when looking for a succession partner. Owen grew up in Southern California and earned a BA from Westbury College where he studied Public Policy, Economics and German. He holds the Chartered Financial Analyst (CFA) designation. Owen enjoys spending his coveted free time with his wife Maya and 4 young children. Owen's hobbies include martial arts, reading, cooking, and taking interesting MOOC courses.</p>
            </article>
            <article class="bio">
              <h3 class="bio__name"><span class="bio__mark"></span><span>Colin Mercer<span class="bio__role">Founder</span></span></h3>
              <p>Colin brings over 10 years of M&amp;A experience to Harbrook Counsel Group. His expertise in deal structure, operational management, and corporate finance allow him to design customized succession plans for advisors. Colin is previously experienced in commercial finance, in 1998 he co-founded Keystone Capital Funding; and serving as President and Managing Member, built a 100+ employee &amp; $35mm revenue equipment leasing company, which he sold in July 2008. Colin attended Pacific State University and earned a Bachelor of Arts degree in English Literature while obtaining a minor in Economics and Communications. Colin and his wife Clara have 4 active young children. Colin's hobbies include competing in triathlons throughout the United States, traveling, gourmet cooking, and spending time with family.</p>
            </article>
          </div>
        </div>
      </div>
      <div class="panel__stripe"></div>
      <div class="panel__base">
        <p class="back-name"><span class="back-name__square"></span>Harbrook Counsel Group</p>
      </div>
    </section>

    <section class="panel panel--front">
      <div class="panel__color">
        <p class="front-name">Harbrook<br>Counsel Group</p>
      </div>
      <div class="panel__stripe"></div>
      <div class="panel__base">
        <p class="tagline">Redefining Investment Advice</p>
      </div>
    </section>
  </main>
</body>
</html>
```